Rivolex.com Trucking Company Website

Need a website designed (no content) for a trucking company, specializing in trucking of ocean containers (intermodal Trucking). Heavy emphasis on technology, using latest technology, providing unabated visibility and realtime information.
clean minimalist industrial website
example:
https://www.bramtiq.com/

Target Market(s)

Professional Business Consumer corporate and small business

Industry/Entity Type

Trucking Company

Number of Pages Required

5+ page

Requirements
Must have
• Industrial Design, simple informative, for a busy professional to view and get the necessary information with out the distractions.
• Blog Page
• Client Log-In on the front page
• Technology page - showing our intensive investments in technology
Nice to have
• If ANY images included, MUST be USA related. Example if include an image of a truck, ensure its a USA model. Do the research.
• included our business card for sample of Logo
• Doesnt not have to be the same color schemes.
Should not have
• moving images

```html
<!DOCTYPE html>
<html lang="en">
<head>
<meta charset="utf-8">
<title>Rivolex — Intermodal Trucking</title>
<link href="https://fonts.googleapis.com/css2?family=Merriweather:wght@400;700&family=Open+Sans:ital,wght@0,400;0,600;0,700;1,400&display=swap" rel="stylesheet">
<style>
:root{
  --blue:#0e8fd6;
  --blue-deep:#1479bf;
  --orange:#f7860b;
  --ink:#3c4250;
  --text:#555b66;
  --muted:#8a8f99;
  --pale:#f2f4f8;
  --panel:#e3e7ef;
  --line:#e1e4ea;
  --white:#ffffff;
  --serif:'Merriweather', Georgia, serif;
  --sans:'Open Sans', Arial, sans-serif;
}
*{box-sizing:border-box;margin:0;padding:0}
html,body{width:1200px;height:3087px;overflow:hidden}
body{font-family:var(--sans);color:var(--text);background:var(--white);position:relative}
section,header,footer,nav{position:relative;width:1200px}

/* Header */
.topbar{height:88px}
.logo{position:absolute;left:99px;top:22px;font-family:var(--sans);font-weight:700;font-size:36px;letter-spacing:1px;color:var(--ink)}
.contact-chip{position:absolute;top:18px;display:flex;gap:14px;align-items:center}
.chip-icon{width:52px;height:52px;border-radius:50%;border:1px solid var(--line);display:flex;align-items:center;justify-content:center}
.chip-label{font-family:var(--serif);font-size:14px;color:var(--ink)}
.chip-value{font-size:12px;color:var(--muted);margin-top:3px}
.nav{height:46px;background:var(--blue)}
.nav ul{list-style:none;position:absolute;left:132px;top:0;display:flex;height:46px;align-items:center}
.nav li{color:var(--white);font-size:13px;margin-right:58px;text-transform:uppercase}
.nav li:nth-child(4){margin-right:62px}
.client-login{position:absolute;left:930px;top:0;width:170px;height:46px;background:var(--orange);color:var(--white);font-size:15px;font-weight:600;display:flex;align-items:center;justify-content:center;gap:10px}

/* Hero */
.hero{height:430px;overflow:hidden}
.hero-photo{position:absolute;inset:0;background:linear-gradient(180deg,#7fa6cf 0%,#c9d9ea 34%,#b8553f 48%,#2f5b97 62%,#8a3b30 76%,#9aa0a8 90%,#6f747c 100%)}
.hero h1{position:absolute;top:45px;width:100%;text-align:center;font-family:var(--serif);font-size:60px;font-weight:700;color:var(--white);letter-spacing:1px}
.hero p{position:absolute;top:125px;width:100%;text-align:center;color:var(--white);font-size:18px;font-weight:600;line-height:30px}

/* Welcome */
.welcome{height:388px;background:var(--pale)}
.quote-box{position:absolute;left:99px;top:61px;width:363px;height:280px;background:var(--panel);padding:22px 27px}
.quote-box h3{font-family:var(--serif);font-size:18px;font-weight:400;color:var(--ink);margin-bottom:22px}
.field{background:var(--white);height:36px;font-size:11px;color:#a2a7b0;padding:11px 14px;margin-bottom:12px}
.field-row{display:flex;gap:10px}
.field-row .field{flex:1}
.field.tall{height:40px}
.btn-orange{display:inline-block;background:var(--orange);color:var(--white);font-size:12px;font-weight:700;padding:8px 10px;border-radius:3px}
.welcome-copy{position:absolute;left:542px;top:66px;width:562px}
.welcome-copy h2{font-family:var(--serif);font-size:30px;font-weight:700;color:var(--ink)}
.welcome-copy h4{color:var(--blue);font-size:15px;font-weight:400;margin:12px 0 24px}
.welcome-copy p{font-size:11.8px;line-height:25px}
.btn-outline{display:inline-block;margin-top:28px;border:1px solid #b7bcc5;color:#8a8f99;font-size:12px;padding:9px 14px}

/* Section titles */
.section-title{text-align:center;font-family:var(--serif);font-size:32px;font-weight:700;color:var(--ink)}
.section-sub{text-align:center;font-family:var(--serif);font-style:italic;font-size:12px;color:var(--text);margin-top:10px}

/* Services */
.services{height:565px}
.services .section-title{padding-top:62px}
.service{position:absolute;width:290px}
.service h5{font-family:var(--serif);font-size:18px;font-weight:700;color:var(--blue-deep);margin-bottom:12px}
.service p{font-size:12.5px;line-height:25px}
.service.left{text-align:right;left:103px}
.service.right{left:807px}
.dots{position:absolute;top:340px;width:122px;border-top:2px dotted var(--orange)}
.dots::before,.dots::after{content:"";position:absolute;top:-4px;width:6px;height:6px;border-radius:50%;background:var(--orange)}
.dots::before{left:-3px}.dots::after{right:-3px}
.hub{position:absolute;left:437px;top:160px;width:340px;height:340px;border-radius:50%;border:2px dashed var(--line)}
.hub-photo{position:absolute;left:46px;top:46px;width:248px;height:248px;border-radius:50%;background:linear-gradient(160deg,#e8e020 0%,#b9c7d6 38%,#f2f4f6 60%,#4f6b8e 100%);box-shadow:0 0 0 8px #fff,0 0 18px rgba(0,0,0,.12)}
.hub-icon{position:absolute;width:44px;height:44px;border-radius:50%;background:var(--white);border:1px solid var(--line);display:flex;align-items:center;justify-content:center}

/* Why us */
.why{height:389px;background:linear-gradient(180deg,#1c8fd4,#137ec5)}
.why-copy{position:absolute;left:99px;top:72px;width:640px;color:var(--white)}
.why-copy h2{font-family:var(--serif);font-size:30px;font-weight:700}
.why-copy h4{font-size:16px;font-weight:400;margin:6px 0 20px}
.why-copy p{font-size:11.8px;line-height:25px;width:640px}
.feature{position:absolute;top:250px;display:flex;gap:16px;width:320px;color:var(--white)}
.feature-icon{flex:none;width:68px;height:68px;border-radius:10px;background:var(--orange);border:3px solid #fff;display:flex;align-items:center;justify-content:center}
.feature h5{font-family:var(--serif);font-size:16px;font-weight:700;margin-bottom:6px}
.feature p{font-size:12.5px;line-height:23px}
.why-photo{position:absolute;left:793px;top:63px;width:313px;height:262px;border-radius:18px;border:5px solid #fff;background:linear-gradient(135deg,#6a3c7a 0%,#2c2a3a 55%,#181822 100%)}

/* News */
.news{height:534px;background:var(--pale)}
.news .section-title{padding-top:58px}
.news-card{position:absolute;top:174px;width:306px}
.news-img{height:180px;position:relative}
.date-tag{position:absolute;right:14px;top:0;width:52px;height:60px;background:var(--orange);color:var(--white);text-align:center;font-family:var(--serif);font-size:18px;padding-top:8px;line-height:20px}
.date-tag small{display:block;font-size:12px}
.news-card h5{font-family:var(--serif);font-size:17px;font-weight:400;color:#222;margin:22px 0 12px}
.news-card p{font-size:12.5px;line-height:24px}
.news-list{position:absolute;left:795px;top:174px;width:310px}
.news-item{display:flex;gap:18px;height:111px}
.thumb{flex:none;width:86px;height:76px}
.news-item h6{font-family:var(--serif);font-size:13px;font-weight:700;color:#222;line-height:21px}
.news-item .meta{font-size:10px;color:var(--muted);margin:3px 0 3px}
.news-item .more{font-size:12px;font-weight:600;color:var(--blue)}

/* Trucking band */
.band{height:200px}
.band h2{position:absolute;top:60px;width:100%;text-align:center;font-family:var(--serif);font-size:34px;font-weight:700;color:#1e222a}
.band p{position:absolute;top:115px;width:100%;text-align:center;font-family:var(--serif);font-size:18px;color:#7b808a;text-transform:uppercase}
.band p span{color:var(--blue-deep)}
.band-rule{position:absolute;left:0;top:200px;width:1200px;border-top:2px solid var(--orange)}
.contact-now{position:absolute;left:508px;top:181px;width:186px;height:40px;background:var(--orange);color:var(--white);font-size:15px;font-weight:600;display:flex;align-items:center;justify-content:center}

/* Footer */
.footer{height:390px}
.footer .logo{top:84px}
.footer-about{position:absolute;left:97px;top:160px;width:320px;font-size:12.5px;line-height:25px}
.social{position:absolute;left:97px;top:308px;display:flex;gap:12px}
.social span{width:32px;height:32px;border-radius:50%;background:#2a2d33}
.f-contact{position:absolute;top:90px;display:flex;align-items:center;gap:16px;font-size:12px;color:var(--text);line-height:20px}
.f-icon{flex:none;width:40px;height:40px;border-radius:50%;background:#2f3238;display:flex;align-items:center;justify-content:center}
.f-rule{position:absolute;left:455px;top:155px;width:745px;border-top:1px solid var(--line)}
.f-col{position:absolute;top:185px}
.f-col h6{font-family:var(--serif);font-size:17px;font-weight:400;color:#222;margin-bottom:12px;text-transform:uppercase}
.f-col li{list-style:none;font-size:12.5px;line-height:30px}
.f-col .hint{font-size:12.5px}
.email-field{width:238px;height:36px;background:var(--pale);font-size:11px;color:#a2a7b0;padding:11px 14px;margin:14px 0 10px}
.subscribe{width:238px;height:36px;background:var(--blue);color:var(--white);font-size:15px;font-weight:700;display:flex;align-items:center;justify-content:center}
.copyright{position:absolute;left:0;top:3030px;width:1200px;height:57px;border-top:1px solid var(--line);text-align:center;font-size:12px;line-height:56px;color:var(--text)}
</style>
</head>
<body>

<header class="topbar">
  <div class="logo">RIVOLEX</div>
  <div class="contact-chip" style="left:678px">
    <div class="chip-icon"><svg width="22" height="22" viewBox="0 0 22 22"><circle cx="11" cy="11" r="11" fill="#f7860b"/><rect x="6" y="7.5" width="10" height="7" fill="#fff"/><path d="M6 7.5l5 4 5-4" stroke="#f7860b" fill="none"/></svg></div>
    <div><div class="chip-label">EMAIL</div><div class="chip-value">Companyname@mail.com</div></div>
  </div>
  <div class="contact-chip" style="left:937px">
    <div class="chip-icon"><svg width="18" height="18" viewBox="0 0 24 24"><path d="M6.6 10.8a15 15 0 006.6 6.6l2.2-2.2c.3-.3.7-.4 1-.2 1.1.4 2.3.6 3.6.6.6 0 1 .4 1 1V20c0 .6-.4 1-1 1A17 17 0 013 4c0-.6.4-1 1-1h3.5c.6 0 1 .4 1 1 0 1.3.2 2.5.6 3.6.1.3 0 .7-.2 1z" fill="#0e8fd6"/></svg></div>
    <div><div class="chip-label">CALL NOW</div><div class="chip-value">(555) 301 744 218</div></div>
  </div>
</header>

<nav class="nav">
  <ul><li>Home</li><li>About us</li><li>Service</li><li>Project</li><li>Testimonial</li><li>Blog</li><li>Contact us</li></ul>
  <div class="client-login"><svg width="14" height="15" viewBox="0 0 14 15"><circle cx="7" cy="4" r="3.5" fill="#fff"/><path d="M0 15c0-4 3-6.5 7-6.5s7 2.5 7 6.5z" fill="#fff"/></svg>CLIENT LOGIN</div>
</nav>

<section class="hero">
  <div class="hero-photo" role="img" aria-label="Container yard with stacked shipping containers and a blue truck hauling a red container under a blue sky"></div>
  <h1>WE ARE RIVOLEX</h1>
  <p>Using latest technology, providing unabated visibility<br>and realtime information</p>
</section>

<section class="welcome">
  <form class="quote-box">
    <h3>GET A QUOTE</h3>
    <div class="field-row"><div class="field">Name</div><div class="field">Phone number</div></div>
    <div class="field">Mail ID</div>
    <div class="field tall">Your Message</div>
    <span class="btn-orange">SEND NOW</span>
  </form>
  <div class="welcome-copy">
    <h2>WELCOME TO RIVOLEX</h2>
    <h4>WE HAVE EXPERIENCE IN THIS PASSION</h4>
    <p>It is a long established fact that a reader will be distracted by the readable content of a page when looking at its layout. The point of using Lorem Ipsum is that it has a more-or-less normal distribution of letters, as opposed to using 'Content here, content here', it look like readable English. It is a long established fact that a reader will be distracted by the readable content of a page</p>
    <span class="btn-outline">READ MORE</span>
  </div>
</section>

<section class="services">
  <h2 class="section-title">RIVOLEX SERVICES</h2>
  <div class="section-sub">Lorem ipsum dolor consectetur adipisic</div>

  <div class="service left" style="top:212px"><h5>100% satisfied customers</h5><p>Lorem ipsum dolor sit amet elit eiusmod tempor incididunt ut labore dolore magna aliqua</p></div>
  <div class="service left" style="top:376px"><h5>Reliability</h5><p>Lorem ipsum dolor sit amet elit eiusmod tempor incididunt ut labore dolore magna aliqua</p></div>
  <div class="service right" style="top:212px"><h5>Expertise</h5><p>Lorem ipsum dolor sit amet elit eiusmod tempor incididunt ut labore dolore magna aliqua</p></div>
  <div class="service right" style="top:376px"><h5>Custom Solution</h5><p>Lorem ipsum dolor sit amet elit eiusmod tempor incididunt ut labore dolore magna aliqua</p></div>
  <div class="dots" style="left:215px"></div>
  <div class="dots" style="left:805px"></div>

  <div class="hub">
    <div class="hub-photo" role="img" aria-label="White and yellow trucks at a loading dock"></div>
    <div class="hub-icon" style="left:-4px;top:58px"><svg width="20" height="16" viewBox="0 0 20 16" fill="#777"><circle cx="6" cy="4" r="3"/><circle cx="14" cy="4" r="3"/><path d="M0 15c0-4 2.5-6 6-6s6 2 6 6zM8 15c0-4 2.5-6 6-6s6 2 6 6z"/></svg></div>
    <div class="hub-icon" style="right:-4px;top:58px"><svg width="14" height="20" viewBox="0 0 14 20"><path d="M7 1a6 6 0 00-3.5 10.9V15h7v-3.1A6 6 0 007 1z" fill="none" stroke="#777" stroke-width="1.6"/><rect x="4" y="16.5" width="6" height="2" fill="#777"/></svg></div>
    <div class="hub-icon" style="left:-4px;bottom:58px"><svg width="18" height="14" viewBox="0 0 18 14"><path d="M2 7l5 5L16 2" stroke="#777" stroke-width="3" fill="none"/></svg></div>
    <div class="hub-icon" style="right:-4px;bottom:58px"><svg width="20" height="20" viewBox="0 0 20 20" fill="none" stroke="#777" stroke-width="2"><circle cx="7" cy="8" r="3.5"/><circle cx="14.5" cy="14.5" r="2.5"/></svg></div>
  </div>
</section>

<section class="why">
  <div class="why-copy">
    <h2>WHY PEOPLE CHOOSE US</h2>
    <h4>MORE ABOUT US</h4>
    <p>There are many variations of passages of Lorem Ipsum available, but the majority have suffered alteration in some form, by injected humour, or randomised words which don't look even slightly believable.</p>
  </div>
  <div class="feature" style="left:99px">
    <div class="feature-icon"><svg width="26" height="22" viewBox="0 0 26 22" fill="#fff"><rect x="0" y="5" width="26" height="17" rx="2"/><rect x="9" y="0" width="8" height="6" rx="1" fill="none" stroke="#fff" stroke-width="2"/></svg></div>
    <div><h5>Professional company</h5><p>There are many variations passages of Lorem Ipsum available</p></div>
  </div>
  <div class="feature" style="left:433px">
    <div class="feature-icon"><svg width="28" height="20" viewBox="0 0 28 20" fill="#fff"><rect x="0" y="2" width="17" height="13"/><path d="M18 6h5l5 5v4H18z"/><circle cx="6" cy="17" r="3"/><circle cx="22" cy="17" r="3"/></svg></div>
    <div><h5>Goods Tracking Support</h5><p>There are many variations passages of Lorem Ipsum available</p></div>
  </div>
  <div class="why-photo" role="img" aria-label="Portrait photo of the company founder"></div>
</section>

<section class="news">
  <h2 class="section-title">OUR LATEST NEWS</h2>
  <div class="section-sub">Lorem ipsum dolor consectetur adipisic</div>

  <article class="news-card" style="left:99px">
    <div class="news-img" role="img" aria-label="Port crane lifting a blue shipping container" style="background:linear-gradient(180deg,#c98a3a 0%,#4f6f9a 45%,#2d4f86 75%,#9aa7b6 100%)"><div class="date-tag">16<small>JAN</small></div></div>
    <h5>ESSE CILLUM DOLORE FUGIAT</h5>
    <p>Sed ut perspiciatis unde omnis iste natus error sit voluptatem accusantium doloremque laudantium, totam rem aperiam, eaque</p>
  </article>
  <article class="news-card" style="left:449px">
    <div class="news-img" role="img" aria-label="Red semi truck driving on a forest highway" style="background:linear-gradient(180deg,#bcd3ea 0%,#4f7a3e 40%,#b3372f 62%,#7d8087 100%)"><div class="date-tag">16<small>JAN</small></div></div>
    <h5>ESSE CILLUM DOLORE FUGIAT</h5>
    <p>Sed ut perspiciatis unde omnis iste natus error sit voluptatem accusantium doloremque laudantium, totam rem aperiam, eaque</p>
  </article>

  <div class="news-list">
    <div class="news-item"><div class="thumb" role="img" aria-label="Stacked containers at a terminal" style="background:linear-gradient(180deg,#9bb4cf,#a64a3a 55%,#5a6470)"></div><div><h6>Quis nostrud to exercitation ullamco laboris nisi ut</h6><div class="meta">16 Jan, 2017</div><div class="more">Read More</div></div></div>
    <div class="news-item"><div class="thumb" role="img" aria-label="Truck on a highway" style="background:linear-gradient(180deg,#c3d6ea,#b53a31 55%,#7b7f86)"></div><div><h6>Quis nostrud to exercitation ullamco laboris nisi ut</h6><div class="meta">16 Jan, 2017</div><div class="more">Read More</div></div></div>
    <div class="news-item"><div class="thumb" role="img" aria-label="Convoy of trucks on a road" style="background:linear-gradient(180deg,#d0d9e2,#8d4a3c 55%,#6d7178)"></div><div><h6>Quis nostrud to exercitation ullamco laboris nisi ut</h6><div class="meta">16 Jan, 2017</div><div class="more">Read More</div></div></div>
  </div>
</section>

<section class="band">
  <h2>WE ARE A TRUCKING COMPANY</h2>
  <p>Specializing in <span>trucking of ocean</span> containers</p>
  <div class="band-rule"></div>
  <div class="contact-now">CONTACT US NOW</div>
</section>

<footer class="footer">
  <div class="logo">RIVOLEX</div>
  <p class="footer-about">There are many variations of passages of Lorem Ipsum available, but the majority have suffered alteration in some form, by injected humour, or randomised words. There are many variations</p>
  <div class="social" aria-label="Social links"><span></span><span></span><span></span><span></span><span></span></div>

  <div class="f-contact" style="left:460px"><div class="f-icon"><svg width="12" height="16" viewBox="0 0 12 16"><path d="M6 0a6 6 0 00-6 6c0 4.5 6 10 6 10s6-5.5 6-10a6 6 0 00-6-6z" fill="#fff"/><circle cx="6" cy="6" r="2.2" fill="#2f3238"/></svg></div><div>1740 Harbor Line Rd, Beaconport,<br>FL 33990</div></div>
  <div class="f-contact" style="left:720px"><div class="f-icon"><svg width="14" height="14" viewBox="0 0 24 24"><path d="M6.6 10.8a15 15 0 006.6 6.6l2.2-2.2c.3-.3.7-.4 1-.2 1.1.4 2.3.6 3.6.6.6 0 1 .4 1 1V20c0 .6-.4 1-1 1A17 17 0 013 4c0-.6.4-1 1-1h3.5c.6 0 1 .4 1 1 0 1.3.2 2.5.6 3.6.1.3 0 .7-.2 1z" fill="#fff"/></svg></div><div>555-014-2290</div></div>
  <div class="f-contact" style="left:900px"><div class="f-icon"><svg width="14" height="10" viewBox="0 0 14 10"><rect width="14" height="10" fill="#fff"/><path d="M0 0l7 5 7-5" stroke="#2f3238" fill="none"/></svg></div><div>info@companyname.com</div></div>
  <div class="f-rule"></div>

  <div class="f-col" style="left:476px"><h6>Quicklink</h6><ul><li>Home</li><li>About us</li><li>Services</li><li>Blog</li></ul></div>
  <div class="f-col" style="left:633px"><h6>Services</h6><ul><li>24/7 Support</li><li>Expert review</li><li>Intermodal Trucking</li><li>Ocean containers</li></ul></div>
  <div class="f-col" style="left:864px"><h6>Newsletter</h6><div class="hint">Sign up for our newsletter</div><div class="email-field">Email</div><div class="subscribe">SUBSCRIBE</div></div>
</footer>

<div class="copyright">Copyrights@2017Company Name , All rights Reserved</div>

</body>
</html>
```